Website redesign www.tidecrestpc.com law firm site

Need to redesign the website that I currently have to look more modern and professional. Would also like to be able to make updates and post without having a huge hassle. See current www.tidecrestpc.com. I just think that it looks very immature and it's very templated there's no ability for me to make posts or Add links or anything like that

Target Market(s)

California people looking for a powerhouse attorney in

Industry/Entity Type

Legal

Number of Pages Required

3 page

Font styles to use
Serif
Sans Serif

Colors
ec1f27
000000
ffffff

Requirements
Must have
• Must be mobile friendly. Must look professional and have ability to post links to other websites. Must have ability to post blogs or articles. Would like to be able to read my TallyDock account and also have the ability to upload forms for people to download
Nice to have
• Simple design easy to use and not cluttered with too much text

```html
<!DOCTYPE html>
<html lang="en">
<head>
<meta charset="utf-8">
<title>Tidecrest Law, P.C. — Chico California Attorney</title>
<link rel="stylesheet" href="https://fonts.googleapis.com/css2?family=Raleway:wght@400;500;600;700&family=Open+Sans:wght@400;600&display=swap">
<style>
:root{
  --red:#ec1f27;
  --black:#000000;
  --white:#ffffff;
  --ink:#222222;
  --muted:#777777;
  --dark:#1e1e1e;
  --darker:#141414;
  --line:#e4e4e4;
  --soft:#f3f3f3;
}
*{margin:0;padding:0;box-sizing:border-box}
html,body{width:1200px;height:3854px;overflow:hidden;background:var(--white)}
body{position:relative;font-family:"Open Sans",Arial,sans-serif;color:var(--ink)}
.abs{position:absolute}
h2,h3,h4,.brand,.nav{font-family:"Raleway",Arial,sans-serif}

/* header */
.site-header{left:0;top:0;width:1200px;height:100px;background:var(--white);border-bottom:1px solid var(--line)}
.brand{position:absolute;left:110px;top:26px;color:var(--red);font-weight:600;font-size:34px;letter-spacing:.5px;display:flex;align-items:center;gap:12px}
.brand .mark{width:14px;height:14px;background:var(--red)}
.nav{position:absolute;right:100px;top:38px;display:flex;gap:38px;font-size:15px;color:#444}
.nav .active{color:var(--red)}

/* hero */
.hero{left:0;top:100px;width:1200px;height:527px;background:linear-gradient(135deg,#3a2f2a 0%,#8a6a58 35%,#b89c8a 55%,#4b3a30 100%)}
.hero-shade{left:0;top:100px;width:1200px;height:527px;background:linear-gradient(180deg,rgba(0,0,0,.05),rgba(0,0,0,.45))}
.hero-title{left:0;top:400px;width:1200px;text-align:center;color:var(--white);font-family:"Raleway",sans-serif;font-weight:700;font-size:46px}
.hero-sub{left:0;top:460px;width:1200px;text-align:center;color:var(--white);font-family:"Raleway",sans-serif;font-weight:600;font-size:36px}
.hero-arrows{left:550px;top:528px;display:flex;gap:10px}
.hero-arrows span{width:42px;height:42px;border:2px solid var(--white);border-radius:50%;display:flex;align-items:center;justify-content:center}

/* section headings */
.sec-title{left:0;width:1200px;text-align:center;font-size:26px;font-weight:700;color:var(--ink);letter-spacing:.5px}
.sec-title em{font-style:normal;color:var(--red)}
.sec-sub{left:0;width:1200px;text-align:center;font-size:14px;color:var(--muted)}

/* services */
.service{top:789px;width:229px;height:224px;background:var(--soft);box-shadow:0 3px 10px rgba(0,0,0,.15);text-align:center}
.service svg{margin-top:52px}
.service h4{font-size:18px;font-weight:500;margin-top:20px;color:var(--ink)}
.service.featured{background:var(--red);color:var(--white)}
.service.featured svg{margin-top:40px}
.service.featured h4{color:var(--white);margin-top:14px}
.service.featured p{font-size:12px;line-height:18px;padding:8px 28px 0}

/* who we are */
.who-photo{left:0;top:1079px;width:601px;height:437px;background:linear-gradient(135deg,#6e7781 0%,#c2b49e 45%,#8e7a63 70%,#3f4850 100%)}
.who-panel{left:601px;top:1079px;width:599px;height:437px;background:var(--dark)}
.who-panel h2{position:absolute;left:64px;top:46px;color:var(--white);font-size:26px;font-weight:700}
.who-panel h2 em{font-style:normal;color:var(--red)}
.who-panel p{position:absolute;left:64px;width:470px;color:#a9a9a9;font-size:12.5px;line-height:21px}
.who-feats{position:absolute;left:64px;top:310px;width:470px;display:flex;justify-content:space-between;text-align:center;color:var(--white);font-size:13px}
.who-feats div{width:120px}
.who-feats svg{display:block;margin:0 auto 14px}

/* practice areas */
.practice{width:334px;text-align:center}
.practice .ico{width:70px;height:70px;margin:0 auto;border:2px solid var(--red);display:flex;align-items:center;justify-content:center}
.practice .ico.fill{background:var(--red)}
.practice h4{font-size:17px;font-weight:500;margin-top:26px;color:var(--ink)}
.practice p{font-size:12px;line-height:19px;color:var(--muted);margin:10px auto 0;width:286px;height:58px}
.btn{display:inline-block;margin-top:24px;padding:0 22px;height:36px;line-height:36px;background:var(--red);color:var(--white);font-size:13px}
.btn.ghost{background:var(--white);color:var(--red);border:1px solid var(--red)}
.vline{width:1px;background:var(--line)}
.hline{height:1px;background:var(--line)}

/* testimonial */
.testi-band{left:0;top:2333px;width:1200px;height:507px;background:linear-gradient(90deg,#d9d9d9,#f2f2f2 30%,#f7f7f7 50%,#f2f2f2 70%,#d9d9d9)}
.quote{top:2525px;width:300px;text-align:center}
.quote .avatar{width:78px;height:78px;border-radius:50%;margin:0 auto;border:4px solid var(--white);background:linear-gradient(135deg,#8a6a55,#c9a88f)}
.quote p{font-size:13px;line-height:21px;color:#555;margin-top:20px}
.quote .qm{color:var(--red);font-size:30px;font-family:"Raleway",sans-serif;line-height:1;margin-top:18px}
.quote h5{font-family:"Raleway",sans-serif;font-size:17px;font-weight:500;margin-top:6px}
.quote small{font-size:11px;color:#999}
.quote.faded{opacity:.35;transform:scale(.92)}

/* blog */
.post{background:var(--white);box-shadow:0 3px 12px rgba(0,0,0,.14)}
.post .date{display:inline-block;background:var(--red);color:var(--white);font-size:12px;padding:0 16px;height:26px;line-height:26px;border-radius:13px}
.post h3{font-size:17px;font-weight:500;line-height:24px;margin-top:16px;color:var(--ink)}
.post p{font-size:12px;line-height:19px;color:var(--muted);margin-top:14px}
.img{position:absolute}

/* footer */
.footer{left:0;top:3567px;width:1200px;height:224px;background:var(--dark)}
.footer-bar{left:0;top:3791px;width:1200px;height:63px;background:var(--darker);color:#bbb;font-size:11.5px}
.footer h4{position:absolute;top:40px;color:var(--white);font-size:15px;font-weight:600;letter-spacing:.5px}
.footer ul{position:absolute;top:80px;list-style:none;color:#aaa;font-size:11.5px;line-height:21px}
.badge{position:absolute;background:#d8d8d8}
.field{position:absolute;left:890px;top:80px;width:210px;height:40px;background:#2c2c2c;color:#888;font-size:11px;padding:12px}
.send{position:absolute;left:990px;top:138px;width:110px;height:34px;background:var(--red);color:var(--white);font-size:12px;text-align:center;line-height:34px}
.social{position:absolute;top:16px;display:flex;gap:10px;left:985px}
.social span{width:30px;height:30px;border:1px solid #777;border-radius:50%}
</style>
</head>
<body>

<header class="abs site-header">
  <div class="brand"><span class="mark"></span>Tidecrest Law PC</div>
  <nav class="nav"><span class="active">Home</span><span>Attorney Profile</span><span>Practice Areas</span><span>Client Reviews</span><span>Links</span><span>Contact Us</span></nav>
</header>

<div class="abs hero" role="img" aria-label="Photo of two professionals shaking hands over a desk with law books"></div>
<div class="abs hero-shade"></div>
<h1 class="abs hero-title">Welcome To Tidecrest Law, P.C.</h1>
<div class="abs hero-sub">Chico California Attorney</div>
<div class="abs hero-arrows">
  <span><svg width="14" height="14" viewBox="0 0 14 14"><path d="M9 2 4 7l5 5" fill="none" stroke="#fff" stroke-width="2"/></svg></span>
  <span><svg width="14" height="14" viewBox="0 0 14 14"><path d="m5 2 5 5-5 5" fill="none" stroke="#fff" stroke-width="2"/></svg></span>
</div>

<!-- services -->
<h2 class="abs sec-title" style="top:688px">WE OFFER <em>DIFFERENT SERVICES</em></h2>
<p class="abs sec-sub" style="top:730px">There are many variations of passages of Lorem Ipsum available, but the majority suffered</p>

<div class="abs service" style="left:98px">
  <svg width="70" height="60" viewBox="0 0 70 60" fill="none" stroke="#333" stroke-width="2.5"><path d="M35 4v48M20 52h30M8 12h54M35 8v4"/><path d="M14 12 4 34h20zM56 12 46 34h20z"/><path d="M4 34q10 8 20 0M46 34q10 8 20 0"/></svg>
  <h4>Legal Representation</h4>
</div>
<div class="abs service featured" style="left:355px">
  <svg width="44" height="38" viewBox="0 0 44 38" fill="#fff"><rect x="2" y="10" width="40" height="26" rx="3"/><path d="M15 10V5h14v5" fill="none" stroke="#fff" stroke-width="3"/><rect x="19" y="18" width="6" height="5" fill="#ec1f27"/></svg>
  <h4>Professional</h4>
  <p>It is a long established fact that a reader will be distracted by the readable content page.</p>
</div>
<div class="abs service" style="left:614px">
  <svg width="70" height="56" viewBox="0 0 70 56" fill="#333"><path d="M35 6 2 20l33 14 33-14z"/><path d="M16 28v14q19 10 38 0V28L35 36z"/><path d="M62 22v18" stroke="#333" stroke-width="2.5"/></svg>
  <h4>Legal Study</h4>
</div>
<div class="abs service" style="left:871px">
  <svg width="60" height="64" viewBox="0 0 60 64" fill="#333"><circle cx="30" cy="18" r="13"/><path d="M4 62q0-24 26-24t26 24z"/><path d="m27 38 3 16 3-16z" fill="#fff"/></svg>
  <h4>Talented Advocate</h4>
</div>

<!-- who we are -->
<div class="abs who-photo" role="img" aria-label="Photo of a legal team meeting around a table with documents"></div>
<section class="abs who-panel">
  <h2>WHO <em>WE ARE</em></h2>
  <p style="top:104px">Find the big firm style legal counsel you can work with in your hometown region at Tidecrest Law P.C. in Chico, CA. Attorney Dana M. Reyes, Esq. offers a boutique law firm opportunity for clients who want to enjoy all the advantages of her broad legal experience and education.</p>
  <p style="top:200px">She works closely with clients, and has the knowledge of many areas of law to apply to your situation. This is very helpful when it is necessary to incorporate those different areas of law practice into creating a winning argument.</p>
  <div class="who-feats">
    <div><svg width="34" height="34" viewBox="0 0 34 34" fill="none" stroke="#ec1f27" stroke-width="2.5"><circle cx="17" cy="17" r="14"/><circle cx="17" cy="17" r="7"/><circle cx="17" cy="17" r="1.5" fill="#ec1f27"/></svg>Dedicated Team</div>
    <div><svg width="38" height="34" viewBox="0 0 38 34" fill="none" stroke="#ec1f27" stroke-width="2.5"><circle cx="19" cy="10" r="6"/><path d="M7 32q0-14 12-14t12 14z"/><circle cx="6" cy="14" r="3.5"/><circle cx="32" cy="14" r="3.5"/></svg>Best Advisors</div>
    <div><svg width="34" height="34" viewBox="0 0 34 34" fill="none" stroke="#ec1f27" stroke-width="2.5"><path d="M6 4h7l3 8-4 3q3 6 9 9l3-4 8 3v7q-18 2-26-26z"/></svg>24/7 Supports</div>
  </div>
</section>

<!-- practice areas -->
<h2 class="abs sec-title" style="top:1580px">OUR <em>PRACTICE AREAS</em></h2>
<p class="abs sec-sub" style="top:1622px">There are many variations of passages of Lorem Ipsum available majority suffered</p>

<div class="abs vline" style="left:432px;top:1700px;height:290px"></div>
<div class="abs vline" style="left:766px;top:1700px;height:290px"></div>
<div class="abs hline" style="left:98px;top:2010px;width:1002px"></div>
<div class="abs vline" style="left:432px;top:2030px;height:290px"></div>
<div class="abs vline" style="left:766px;top:2030px;height:290px"></div>

<div class="abs practice" style="left:98px;top:1680px">
  <div class="ico"><svg width="24" height="30" viewBox="0 0 24 30" fill="none" stroke="#ec1f27" stroke-width="2"><path d="M8 2h8l-2 5 4 16-6 5-6-5 4-16z"/></svg></div>
  <h4>Business Law</h4>
  <p>Small and medium sized businesses have many of the same legal issues that affect large businesses, such business structure, contracts, dispute resolution.</p>
  <span class="btn">Read More</span>
</div>
<div class="abs practice" style="left:432px;top:1680px">
  <div class="ico fill"><svg width="32" height="26" viewBox="0 0 32 26" fill="none" stroke="#fff" stroke-width="2"><rect x="3" y="3" width="26" height="16"/><path d="M1 23h30M10 14l4-4 3 3 5-5"/></svg></div>
  <h4>Real Estate Law</h4>
  <p>At Tidecrest Law P.C., we help Californians who need legal advice and representation for Real Estate Law activities, such as closings, contracts, searches.</p>
  <span class="btn ghost">Read More</span>
</div>
<div class="abs practice" style="left:766px;top:1680px">
  <div class="ico"><svg width="32" height="30" viewBox="0 0 32 30" fill="none" stroke="#ec1f27" stroke-width="2"><path d="M2 10 16 2l14 8zM5 12v12M12 12v12M20 12v12M27 12v12M2 27h28"/></svg></div>
  <h4>Bankruptcy</h4>
  <p>If your finances are dwindling to the point where you can no longer pay your bills, and you are getting harassed by collection agents, it is time to visit Tidecrest Law P.C.</p>
  <span class="btn">Read More</span>
</div>

<div class="abs practice" style="left:98px;top:2006px">
  <div class="ico"><svg width="34" height="28" viewBox="0 0 34 28" fill="#ec1f27"><circle cx="10" cy="7" r="5"/><circle cx="24" cy="7" r="5"/><path d="M1 26q0-12 9-12t9 12zM15 26q0-12 9-12t9 12z"/></svg></div>
  <h4>Family Law</h4>
  <p>Family Law is one area of legal concern that brings many people in to see our experienced Chico Family Law Attorney at Tidecrest Law P.C. issues that affect the family.</p>
  <span class="btn">Read More</span>
</div>
<div class="abs practice" style="left:432px;top:2006px">
  <div class="ico"><svg width="32" height="30" viewBox="0 0 32 30" fill="none" stroke="#ec1f27" stroke-width="2"><circle cx="10" cy="20" r="7"/><circle cx="22" cy="10" r="7"/><path d="M15 15l2-1"/></svg></div>
  <h4>Criminal Law</h4>
  <p>If you were charged with a criminal offense, or if you are under investigation for one, it is essential to hire an experienced, qualified attorney at the earliest.</p>
  <span class="btn">Read More</span>
</div>
<div class="abs practice" style="left:766px;top:2006px">
  <div class="ico"><svg width="34" height="24" viewBox="0 0 34 24" fill="none" stroke="#ec1f27" stroke-width="2"><path d="M3 16 9 6h16l6 10z"/><circle cx="10" cy="19" r="3"/><circle cx="24" cy="19" r="3"/></svg></div>
  <h4>Civil Litigation</h4>
  <p>Civil litigation is a vast legal category than can include everything from personal injury cases to tort reform. No matter the nature of the case, the legal process.</p>
  <span class="btn">Read More</span>
</div>

<!-- testimonial -->
<div class="abs testi-band" role="img" aria-label="Soft grey background photo of a courthouse colonnade"></div>
<h2 class="abs sec-title" style="top:2394px">OUR CLIENT <em>TESTIMONIAL</em></h2>
<p class="abs sec-sub" style="top:2436px">There are many variations of passages of Lorem Ipsum available majority suffered</p>

<div class="abs quote faded" style="left:80px;top:2500px">
  <div class="avatar" role="img" aria-label="Client portrait"></div>
  <p>"Contrary to popular belief, Lorem Ipsum is not simply random text. It has roots in a piece of classical Latin literature from 45 BC, making it over 2000 years old. Martin Ellery, a Latin professor at Brookfield College in Virginia"</p>
  <div class="qm">&ldquo;</div><h5>Chirs Doe</h5><small>Startup CEO</small>
</div>
<div class="abs quote" style="left:450px">
  <div class="avatar" role="img" aria-label="Client portrait"></div>
  <p>" Contrary to popular belief, Lorem Ipsum is not simply random text. It has roots in a piece of classical Latin literature from 45 BC, making it over 2000 years old. Martin Ellery, a Latin professor at Brookfield College in Virginia "</p>
  <div class="qm">&ldquo;</div><h5>Chirs Doe</h5><small>Startup CEO</small>
</div>
<div class="abs quote faded" style="left:820px;top:2500px">
  <div class="avatar" role="img" aria-label="Client portrait"></div>
  <p>"Contrary to popular belief, Lorem Ipsum is not simply random text. It has roots in a piece of classical Latin literature from 45 BC, making it over 2000 years old. Martin Ellery, a Latin professor at Brookfield College in Virginia"</p>
  <div class="qm">&ldquo;</div><h5>Chirs Doe</h5><small>Startup CEO</small>
</div>

<!-- blog -->
<h2 class="abs sec-title" style="top:2892px">OUR <em>LATEST BLOG</em></h2>
<p class="abs sec-sub" style="top:2936px">There are many variations of passages of Lorem Ipsum</p>

<article class="abs post" style="left:98px;top:2989px;width:642px;height:254px">
  <div class="img" style="left:0;top:0;width:283px;height:254px;background:linear-gradient(135deg,#e7ddd0,#b69d7f 55%,#5d4a3a)" role="img" aria-label="Photo of a hand signing a document with a pen"></div>
  <div style="position:absolute;left:305px;top:22px;width:310px">
    <span class="date">July 25 , 2016</span>
    <h3>This book is a treatise on the very uch popular theory of ethics</h3>
    <p>There are many variations of passages of Lorem Ipsum available, but the majority have suffered alteration in some form, by injected humour, or randomised words which don't look even.</p>
  </div>
</article>
<div class="abs post img" style="left:766px;top:2989px;width:334px;height:254px;background:linear-gradient(135deg,#6b3d22,#a8693c 40%,#3a2a24)" role="img" aria-label="Photo of a lawyer holding books in front of a law library shelf"></div>

<article class="abs post" style="left:98px;top:3266px;width:642px;height:247px">
  <div style="position:absolute;left:26px;top:22px;width:310px">
    <span class="date">July 25 , 2016</span>
    <h3>This book is a treatise on the very uch popular theory of ethics</h3>
    <p>There are many variations of passages of Lorem Ipsum available, but the majority have suffered alteration in some form, by injected humour, or randomised words which don't look even.</p>
  </div>
  <div class="img" style="left:365px;top:0;width:277px;height:247px;background:linear-gradient(135deg,#8b8f96,#d8d6d1 45%,#5a4f49)" role="img" aria-label="Photo of a smiling attorney seated at a conference table"></div>
</article>
<article class="abs post" style="left:766px;top:3266px;width:334px;height:247px">
  <div style="position:absolute;left:26px;top:22px;width:285px">
    <span class="date">July 25 , 2016</span>
    <h3>This book is a treatise on the very uch popular theory of ethics</h3>
    <p>There are many variations of passages of Lorem Ipsum available, but the majority have suffered alteration in some form, by injected humour, or randomised words which don't look even.</p>
  </div>
</article>

<!-- footer -->
<footer class="abs footer">
  <div class="badge" style="left:98px;top:52px;width:120px;height:120px;border-radius:50%;background:#cfcfcf"></div>
  <div class="badge" style="left:235px;top:70px;width:170px;height:34px"></div>
  <div class="badge" style="left:235px;top:120px;width:170px;height:34px"></div>
  <h4 style="left:465px">COMMUNITY</h4>
  <ul style="left:465px"><li>Suggtines</li><li>Terms and conditions</li><li>privacy policy</li><li>site map</li><li>Contact us</li></ul>
  <h4 style="left:640px">CONTACT US</h4>
  <ul style="left:640px"><li>Address : 200 Oak Street, combined</li><li>with a handful Lane</li><li>Ph : (000) 555-0143</li><li>Fax : (000) 555-0144</li></ul>
  <h4 style="left:890px">NEWSLETTER</h4>
  <div class="field">Enter The Email Id</div>
  <div class="send">Send Now</div>
</footer>
<div class="abs footer-bar">
  <span style="position:absolute;left:98px;top:24px">Copyrights@2016Company name all rights reserved &nbsp;|&nbsp; Legal Disclimer Privacy</span>
  <div class="social"><span></span><span></span><span></span></div>
</div>

</body>
</html>
```